Tervolan Pty Ltd professional business card

A professional business card template using the colours from the supplied logo.
Clean crisp lines while, Modern while not being over the top.

Target Market(s)

Construction, commerical and industrial

Industry/Entity Type

Communications

Contact Information for Business Card

For a Communications, IT, Optical fibre installation company

Colors
37b8a4

```html
<!DOCTYPE html>
<html lang="en">
<head>
<meta charset="utf-8">
<title>Tervolan Pty Ltd – Business Card</title>
<link href="https://fonts.googleapis.com/css2?family=Montserrat:wght@400;500;600&family=Tinos:wght@700&display=swap" rel="stylesheet">
<style>
  :root {
    --backdrop-light: #d2d2d2;
    --backdrop-dark: #a4a4a4;
    --card: #131313;
    --teal: #2196a6;
    --teal-rule: #1d5d66;
    --white: #ffffff;
  }
  * { box-sizing: border-box; margin: 0; padding: 0; }
  html, body { width: 1200px; height: 801px; overflow: hidden; }
  body {
    background: linear-gradient(180deg, var(--backdrop-light), var(--backdrop-dark));
    font-family: "Montserrat", sans-serif;
    color: var(--white);
    position: relative;
  }
  .card {
    position: absolute;
    top: 246px;
    width: 540px;
    height: 309px;
    background: var(--card);
    border-radius: 24px;
    border-bottom: 4px solid var(--teal);
    box-shadow: 0 14px 30px rgba(0,0,0,.35);
    overflow: hidden;
  }
  .card--front { left: 40px; }
  .card--back { left: 620px; }

  .wordmark {
    font-weight: 600;
    letter-spacing: .04em;
    color: var(--white);
    display: flex;
    align-items: center;
    gap: 10px;
    position: absolute;
  }
  .wordmark__dot {
    border-radius: 50%;
    background: var(--teal);
    display: inline-block;
  }
  .card--front .wordmark { top: 58px; left: 200px; font-size: 34px; }
  .card--front .wordmark__dot { width: 18px; height: 18px; }
  .card--back .wordmark { top: 50%; left: 50%; transform: translate(-50%, -50%); font-size: 52px; }
  .card--back .wordmark__dot { width: 26px; height: 26px; }

  .divider {
    position: absolute;
    top: 176px;
    left: 40px;
    right: 40px;
    height: 1px;
    background: var(--teal-rule);
  }
  .identity { position: absolute; left: 40px; top: 124px; }
  .identity__name {
    font-family: "Tinos", serif;
    font-weight: 700;
    font-size: 22px;
    color: var(--teal);
    letter-spacing: .02em;
    text-transform: uppercase;
    line-height: 1;
  }
  .identity__role { font-size: 13px; margin-top: 6px; }

  .contacts { position: absolute; left: 40px; top: 190px; list-style: none; }
  .contacts li {
    display: flex; align-items: center; gap: 8px;
    font-size: 12px; line-height: 1; margin-bottom: 8px;
  }
  .contacts svg { width: 11px; height: 11px; fill: var(--teal); flex: none; }

  .address {
    position: absolute; right: 40px; bottom: 34px;
    text-align: right; font-size: 12px; line-height: 1.5;
  }
</style>
</head>
<body>
  <section class="card card--front" aria-label="Business card front">
    <div class="wordmark"><span class="wordmark__dot"></span>TERVOLAN</div>
    <div class="identity">
      <p class="identity__name">Marek Dalby</p>
      <p class="identity__role">General Manager</p>
    </div>
    <div class="divider"></div>
    <ul class="contacts">
      <li><svg viewBox="0 0 12 12"><path d="M2 1h2l1 3-1.3 1A6 6 0 0 0 7 8.3L8 7l3 1v2a1 1 0 0 1-1 1A9 9 0 0 1 1 2a1 1 0 0 1 1-1z"/></svg>(512) 555-0148</li>
      <li><svg viewBox="0 0 12 12"><path d="M3 0h6a1 1 0 0 1 1 1v10a1 1 0 0 1-1 1H3a1 1 0 0 1-1-1V1a1 1 0 0 1 1-1zm0 2v7h6V2z"/></svg>(512) 555-0172</li>
      <li><svg viewBox="0 0 12 12"><path d="M0 2h12v8H0zm1 1v.4l5 3.3 5-3.3V3z"/></svg>contact@tervolan.com.au</li>
      <li><svg viewBox="0 0 12 12"><path d="M6 0a6 6 0 1 0 0 12A6 6 0 0 0 6 0zm0 1.2c.8.9 1.3 2.5 1.4 4.2H4.6C4.7 3.7 5.2 2.1 6 1.2zM4.6 6.6h2.8C7.3 8.3 6.8 9.9 6 10.8c-.8-.9-1.3-2.5-1.4-4.2z"/></svg>www.tervolan.com.au</li>
    </ul>
    <address class="address" style="font-style:normal">
      18 Kestrel Bay Rd<br>Harbour View, CT 558210
    </address>
  </section>

  <section class="card card--back" aria-label="Business card back">
    <div class="wordmark"><span class="wordmark__dot"></span>TERVOLAN</div>
  </section>
</body>
</html>
```